Chic streamline modern edgy! Danemerecurls.com

I need a website built for my personal business. I am a hair stylist and I would like a crisp website that works well, is sleek, easy to use, and allows my clients to navigate through Services and pay deposits for services listed.

My logo is somewhat of a full moon, so my theme is nocturnal.

My information can be found at chairbook.com/danemerecurls

Target Market(s)

Women ages 25-55 who are looking for luxury hair extension services

Industry/Entity Type

Hair And Beauty

Number of Pages Required

1 page

Colors
474747
919191
d3d3d3
000000

Requirements
Must have
• Location map, coinvale link embedded for deposits, contact box, bio, faq/policies, menu of services, hours of availability by appointment only .
Nice to have
• An interactive calander where I could post dates that I am available, preferred providers for other beauty services where i could list other websites for make up and other beauty related referrals. a bridal tab would be nice to offer information about bridal services and policies.

```html
<!DOCTYPE html>
<html lang="en">
<head>
<meta charset="utf-8">
<title>Danemere Curls</title>
<link href="https://fonts.googleapis.com/css2?family=Barlow:wght@300;400;500;600;700&display=swap" rel="stylesheet">
<style>
:root{
  --black:#000000;
  --charcoal:#474747;
  --slate:#919191;
  --silver:#d3d3d3;
  --panel:#1d1d1d;
  --card:#2a2a2a;
  --deep:#111111;
  --red:#d0021b;
  --white:#ffffff;
}
*{box-sizing:border-box;margin:0;padding:0}
html,body{width:1200px;height:2772px;overflow:hidden}
body{position:relative;background:var(--black);color:var(--silver);font-family:'Barlow',Arial,sans-serif}
.abs{position:absolute}

/* header */
.sidebar{left:0;top:0;width:300px;height:720px;background:var(--charcoal)}
.brand{left:0;top:40px;width:300px;text-align:center}
.brand-mark{width:64px;height:64px;border-radius:50%;background:var(--silver);margin:0 auto 14px}
.brand-name{font-size:26px;font-weight:500;letter-spacing:4px;color:var(--white);text-transform:uppercase}
.side-nav{left:160px;top:270px;list-style:none}
.side-nav li{font-size:15px;color:var(--silver);line-height:24px}
.hero{left:300px;top:0;width:900px;height:720px;background:linear-gradient(120deg,#1a1a1a 0%,#5a5a5a 45%,#9a9a9a 62%,#3a3a3a 100%)}
.pay-tag{left:1020px;top:648px;font-size:24px;font-weight:600;color:var(--white);display:flex;align-items:center;gap:10px}
.pay-tag span.dot{width:18px;height:18px;background:var(--white)}

/* about row */
.portrait{left:0;top:720px;width:380px;height:220px;background:linear-gradient(90deg,#3a3a3a,#6e6e6e 50%,#2a2a2a)}
.bio{left:380px;top:720px;width:540px;height:220px;background:var(--panel);padding:44px 24px 0 28px}
.bio h2{font-size:20px;font-weight:500;color:var(--white);margin-bottom:6px}
.bio p{font-size:11px;line-height:15px;color:var(--slate)}
.calendar{left:920px;top:720px;width:280px;height:220px;background:var(--panel);padding:26px 24px}
.cal-title{font-size:11px;text-align:center;color:var(--silver);letter-spacing:2px;margin-bottom:6px}
.cal-grid{display:grid;grid-template-columns:repeat(7,1fr);gap:4px}
.cal-grid span{height:18px;background:#3a3a3a}
.cal-grid span.on{background:var(--red)}
.cal-grid span.head{height:12px;background:transparent;font-size:9px;text-align:center;color:var(--slate)}

/* hours + map */
.hours{left:0;top:940px;width:380px;height:300px;background:var(--deep);padding:136px 0 0 56px}
.hours h3{font-size:15px;font-weight:500;color:var(--white);margin-bottom:4px}
.hours table{border-collapse:collapse;font-size:12px;color:var(--silver)}
.hours td{padding:1px 26px 1px 0}
.map{left:380px;top:940px;width:820px;height:280px;background:linear-gradient(135deg,#e7e5df,#d6d3cc 60%,#cfd9c8)}
.map-strip{left:380px;top:1220px;width:820px;height:20px;background:var(--deep)}

/* services */
.services-title{left:0;top:1310px;width:1200px;text-align:center;font-size:30px;font-weight:400;color:var(--white)}
.cat{font-size:11px;font-weight:600;letter-spacing:1px;color:var(--white)}
.card{width:336px;height:232px;background:var(--card);padding:18px 22px}
.card h4{font-size:24px;font-weight:400;color:var(--white);margin-bottom:10px}
.card p{font-size:10px;line-height:13px;color:var(--silver);height:52px;overflow:hidden}
.price{position:absolute;left:22px;bottom:20px;font-size:22px;line-height:26px;color:var(--white)}
.request{position:absolute;right:16px;bottom:24px;background:var(--red);color:var(--white);font-size:14px;font-weight:600;padding:6px 10px;letter-spacing:.5px}

/* testimonial */
.testimonial{left:0;top:2320px;width:1200px;height:220px;background:#262626}
.t-name{left:160px;top:2396px;font-size:38px;font-weight:400;color:var(--slate)}
.t-date{left:260px;top:2452px;font-size:14px;color:var(--slate)}
.t-quote{left:600px;top:2380px;width:560px;font-size:17px;line-height:24px;color:var(--slate)}

/* footer */
.footer{left:0;top:2540px;width:1200px;height:232px;background:var(--black)}
.foot-nav{left:40px;top:2614px;font-size:17px;font-weight:600;color:var(--white)}
.social{left:980px;top:2600px;display:flex;gap:14px}
.social span{width:48px;height:48px;border-radius:50%;background:var(--charcoal)}
.foot-rule{left:0;top:2680px;width:1200px;height:1px;background:#222}
.foot-addr{left:40px;top:2700px;font-size:11px;color:var(--slate)}
.foot-copy{left:880px;top:2700px;font-size:11px;color:var(--slate)}
</style>
</head>
<body>

<div class="abs sidebar"></div>
<div class="abs brand">
  <div class="brand-mark"></div>
  <div class="brand-name">Danemere Curls</div>
</div>
<ul class="abs side-nav">
  <li>Biography</li>
  <li>Contact</li>
  <li>Calendar</li>
  <li>Services</li>
  <li>Book an Appointment</li>
  <li>FAQ</li>
</ul>
<div class="abs hero" role="img" aria-label="Portrait of a model with long glossy dark hair, black and white"></div>
<div class="abs pay-tag"><span class="dot"></span>Coinvale</div>

<div class="abs portrait" role="img" aria-label="Portrait of the stylist"></div>
<div class="abs bio">
  <h2>Biography</h2>
  <p>Danemere Curls is a luxury hair studio built on a love for healthy, beautiful hair. With years of experience in extensions, color and specialty curls, every appointment is tailored to the client, from consultation to finish. Our goal is a look that lasts, a process that feels calm and a result that makes you feel confident every single day. Services are offered by appointment only, with care given to the health of your natural hair throughout.</p>
</div>
<div class="abs calendar">
  <div class="cal-title">APRIL 2016</div>
  <div class="cal-grid">
    <span class="head">S</span><span class="head">M</span><span class="head">T</span><span class="head">W</span><span class="head">T</span><span class="head">F</span><span class="head">S</span>
    <span></span><span></span><span></span><span></span><span></span><span class="on"></span><span class="on"></span>
    <span></span><span></span><span class="on"></span><span class="on"></span><span></span><span class="on"></span><span class="on"></span>
    <span></span><span></span><span class="on"></span><span></span><span class="on"></span><span class="on"></span><span></span>
    <span></span><span></span><span class="on"></span><span class="on"></span><span></span><span class="on"></span><span class="on"></span>
    <span></span><span></span><span></span><span></span><span></span><span></span><span></span>
  </div>
</div>

<div class="abs hours">
  <h3>Business Hours</h3>
  <table>
    <tr><td>Tuesday</td><td>7:00am</td><td>—</td><td>7:00pm</td></tr>
    <tr><td>Wednesday</td><td>7:00am</td><td>—</td><td>7:00pm</td></tr>
    <tr><td>Thursday</td><td>7:00am</td><td>—</td><td>7:00pm</td></tr>
    <tr><td>Friday</td><td>7:00am</td><td>—</td><td>7:00pm</td></tr>
    <tr><td>Saturday</td><td>7:00am</td><td>—</td><td>7:00pm</td></tr>
  </table>
</div>
<div class="abs map" role="img" aria-label="Location map of the studio"></div>
<div class="abs map-strip"></div>

<div class="abs services-title">Services and Book an Appointment</div>

<div class="abs cat" style="left:72px;top:1382px">ADJUSTMENTS</div>
<div class="abs cat" style="left:792px;top:1382px">ARRANGEMENTS</div>
<div class="abs card" style="left:72px;top:1404px"><h4>Relaxer</h4><p>For current clients with relaxed hair. Deep conditioning treatment and trim included. Additional time may be required depending on density.</p><div class="price">$100 and up<br>2 hr.</div><div class="request">REQUEST</div></div>
<div class="abs card" style="left:432px;top:1404px"><h4>Extension removal</h4><p>Removal of sewn-in extensions. Wash, deep condition, trim, and natural hair assessment are included. This service is ideal for clients ready to refresh.</p><div class="price">$85 and up<br>1 hr., 45 min.</div><div class="request">REQUEST</div></div>
<div class="abs card" style="left:792px;top:1404px"><h4>Consultation</h4><p>Hair consultations can be in-person and are required for new clients. This is the perfect way for me to gauge your goals.</p><div class="price">$55<br>15 min.</div><div class="request">REQUEST</div></div>

<div class="abs cat" style="left:72px;top:1694px">ATTACHMENTS</div>
<div class="abs cat" style="left:432px;top:1694px">ENHANCEMENTS</div>
<div class="abs cat" style="left:792px;top:1694px">UPGRADES</div>
<div class="abs card" style="left:72px;top:1716px"><h4>Extensions</h4><p>Extensions, done correctly, are a great way to protect and grow your natural hair. Using a braiding technique that prevents damage.</p><div class="price">$275 and up<br>3 hr.</div><div class="request">REQUEST</div></div>
<div class="abs card" style="left:432px;top:1716px"><h4>Color services</h4><p>In-person consultation required for new clients. Single process color includes the application of permanent or semi-permanent color.</p><div class="price">$125 and up<br>2 hr.</div><div class="request">REQUEST</div></div>
<div class="abs card" style="left:792px;top:1716px"><h4>Extension Straightening</h4><p>For extremely curly extension clients who desire a sleek straight look or a curl that is looser than the natural texture.</p><div class="price">$50 and up<br>45 min.</div><div class="request">REQUEST</div></div>

<div class="abs card" style="left:72px;top:2036px"><h4>Hair Cut</h4><p>Ready for a new look? This service is currently paired with a shampoo set, great for pre-existing extensions and natural hair.</p><div class="price">$35 and up<br>45 min.</div><div class="request">REQUEST</div></div>
<div class="abs card" style="left:432px;top:2036px"><h4>Specialty Curls</h4><p>Wand Curls</p><div class="price">$25 and up<br>1 hr.</div><div class="request">REQUEST</div></div>
<div class="abs card" style="left:792px;top:2036px"><h4>specialty styles</h4><p>Updo styling ideal for special events.</p><div class="price">$55 and up<br>45 min.</div><div class="request">REQUEST</div></div>

<div class="abs testimonial"></div>
<div class="abs t-name">Marisol T.</div>
<div class="abs t-date">7/08/15</div>
<div class="abs t-quote">"I will not let anyone else do my hair but her. The braiding foundation is everything!!! She is so sweet and you are truly entertained in her chair. I love her! Definitely book your next appointment here!"</div>

<div class="abs footer"></div>
<div class="abs foot-nav">HOME | Contact and Biography | Calendar | Services and Book an Appointment | FAQ |</div>
<div class="abs social"><span></span><span></span><span></span></div>
<div class="abs foot-rule"></div>
<div class="abs foot-addr">Address: 1480 Lunaria Avenue, Suite 3, Halvern · 555-0148</div>
<div class="abs foot-copy">© 2016 Danemerecurls.com. All rights reserved.</div>

</body>
</html>
```